SEAFOOD PACKAGING (Products for consumer)

We are looking to create packaging for various seafood products such as octopus and squid. We plan to sell our products in upscale supermarkets.

We are specializing in cut octopus this time.

Please include our company logo. Also, please leave a transparent area so that customers can see the product inside.
Updates

We want to show what is inside, so a picture of the octopus is not required. We need something simple and sophisticated.

Target Market(s)

upscale store in US and ASIA

Industry/Entity Type

Fisheries dealer

Requirements
Must have
• Please include the attached logo,Blue one is preferred.Please leave a transparent part so that the contents of the product can be seen by the consumer.1. product name on packaging →CUT OCTOPUS,TAKO SASHIMI,Highest quality,Top quality etc... 3. What text information should be on the packaging →(It may be edited, but this is the image) The raw materials are caught in a very clean environment and processed in a modern factory with ZEK certification. We are committed to additive-free products. 4. Packing size(cm/inch)→it will be about 19cm*22cm. 5. what kind of packaging do you use →PP or PA 6. dll →ai,jag
Nice to have
• https://quillmora.example/shots/4829174-Velka-Reef We need something simple and sophisticated like this one.
Should not have
• We want to show what is inside, so a picture of the octopus is not required. We need something simple and sophisticated.

```html
<!DOCTYPE html>
<html lang="en">
<head>
<meta charset="utf-8">
<title>Kairo Cut Octopus – Tako Sashimi Pack</title>
<link rel="stylesheet" href="https://fonts.googleapis.com/css2?family=Josefin+Sans:wght@600;700&family=Roboto+Condensed:wght@400;700&display=swap">
<style>
  :root {
    --backdrop: #939598;
    --pack-blue: #1f5fae;
    --brand-blue: #1a6fc2;
    --pack-white: #fbf9f8;
    --window-grey: #dcdde0;
    --text-white: #ffffff;
  }
  * { box-sizing: border-box; margin: 0; padding: 0; }
  html, body {
    width: 1200px; height: 900px; overflow: hidden;
    background: var(--backdrop);
  }
  .pack-front {
    position: absolute; left: 237px; top: 31px;
    width: 725px; height: 838px;
  }
  .pack-shapes { position: absolute; inset: 0; width: 725px; height: 838px; }
  .pack-text {
    position: absolute; left: 0; width: 100%;
    color: var(--text-white); text-align: center;
  }
  .brand {
    position: absolute; top: 38px; left: 0; width: 100%;
    display: flex; justify-content: center; align-items: center; gap: 18px;
  }
  .brand-dot {
    width: 38px; height: 38px; border-radius: 50%;
    background: var(--brand-blue);
  }
  .brand-name {
    font-family: "Josefin Sans", sans-serif; font-weight: 700;
    font-size: 84px; line-height: 1; letter-spacing: 6px;
    color: var(--brand-blue); padding-top: 10px;
  }
  .product-name {
    top: 188px;
    font-family: "Josefin Sans", sans-serif; font-weight: 700;
    font-size: 80px; line-height: 1; letter-spacing: 1px;
  }
  .product-subname {
    top: 264px;
    font-family: "Josefin Sans", sans-serif; font-weight: 700;
    font-size: 56px; line-height: 1; letter-spacing: 1px;
  }
  .claims {
    top: 328px;
    font-family: "Josefin Sans", sans-serif; font-weight: 600;
    font-size: 17px; letter-spacing: 1px;
  }
  .claims .sep { margin: 0 18px; }
  .origin-note {
    left: 179px; width: 380px; top: 708px; text-align: left;
    font-family: "Roboto Condensed", sans-serif; font-size: 12px;
    line-height: 16px; letter-spacing: 0.2px;
    padding-bottom: 6px; border-bottom: 1.5px solid var(--text-white);
  }
  .promise {
    left: 179px; width: 370px; top: 753px;
    font-family: "Roboto Condensed", sans-serif; font-size: 12px;
    letter-spacing: 0.3px;
  }
  .net-weight {
    left: 179px; width: 370px; top: 781px;
    font-family: "Roboto Condensed", sans-serif; font-weight: 700;
    font-size: 17px; letter-spacing: 0.8px;
  }
</style>
</head>
<body>
  <main class="pack-front">
    <svg class="pack-shapes" viewBox="0 0 725 838" aria-hidden="true">
      <rect class="pack-base" x="0" y="0" width="725" height="838" fill="var(--pack-blue)"/>
      <path class="top-header" d="M0,0 H725 V106 C600,125 470,160 360,156 C230,152 110,115 0,112 Z" fill="var(--pack-white)"/>
      <path class="clear-window" d="M0,362 H725 V690 a40.3,22 0 0 0 -80.6,0 a40.3,22 0 0 0 -80.6,0 a40.3,22 0 0 0 -80.6,0 a40.3,22 0 0 0 -80.6,0 a40.3,22 0 0 0 -80.6,0 a40.3,22 0 0 0 -80.6,0 a40.3,22 0 0 0 -80.6,0 a40.3,22 0 0 0 -80.6,0 a40.3,22 0 0 0 -80.2,0 Z" fill="var(--window-grey)"/>
      <path class="window-edge" d="M725,690 a40.3,22 0 0 0 -80.6,0 a40.3,22 0 0 0 -80.6,0 a40.3,22 0 0 0 -80.6,0 a40.3,22 0 0 0 -80.6,0 a40.3,22 0 0 0 -80.6,0 a40.3,22 0 0 0 -80.6,0 a40.3,22 0 0 0 -80.6,0 a40.3,22 0 0 0 -80.6,0 a40.3,22 0 0 0 -80.2,0" fill="none" stroke="var(--pack-white)" stroke-width="5"/>
      <circle class="quality-seal" cx="106" cy="676" r="73" fill="var(--pack-white)"/>
      <circle class="quality-seal-ring" cx="106" cy="676" r="64" fill="none" stroke="var(--pack-blue)" stroke-width="3"/>
    </svg>

    <div class="brand">
      <span class="brand-dot"></span>
      <span class="brand-name">KAIRO</span>
    </div>

    <h1 class="pack-text product-name">CUT OCTOPUS</h1>
    <h2 class="pack-text product-subname">TAKO SASHIMI</h2>
    <p class="pack-text claims">ALL NATURAL<span class="sep">•</span>NO PRESERVATIVES<span class="sep">•</span>NO ADDITIVES</p>

    <p class="pack-text origin-note">THE RAW MATERIALS ARE CAUGHT IN A VERY CLEAN ENVIRONMENT<br>AND PROCESSED IN A MODERN FACTORY WITH ZEK CERTIFICATION</p>
    <p class="pack-text promise">WE ARE COMMITTED TO ADDITIVE-FREE PRODUCTS</p>
    <p class="pack-text net-weight">NET WT 16OZ (1LB) 454G</p>
  </main>
</body>
</html>
```